Business Card Design Project

Hi,
This is a simple contest. The logo for the back of the card is deigned. See attached files. The front of the card must have :

Directors Name: Dorian
Mob:
e-mail:
Postal Address:
Web Page Adress:

It may also add words: "Trusted Partners in Building and Site Delivery Services"

Target Market(s)

Business & Home owners alike

Industry/Entity Type

Business

Requirements
Must have
• See details above and logo attached
Should not have
• Images other than logo

```html
<!DOCTYPE html>
<html lang="en">
<head>
<meta charset="utf-8">
<title>Summit Civil Works Group – Business Card</title>
<link rel="stylesheet" href="https://fonts.googleapis.com/css2?family=Open+Sans:wght@400;700&display=swap">
<style>
  :root {
    --brand-blue: #1b9bd7;
    --brand-blue-soft: #6fc0e8;
    --pale-blue: #bfe2f4;
    --card-grey: #e5e5e5;
    --card-edge: #ffffff;
    --white: #ffffff;
    --stage: #f2f2f2;
  }
  * { box-sizing: border-box; margin: 0; padding: 0; }
  html, body { width: 1200px; height: 923px; overflow: hidden; }
  body {
    background: var(--stage);
    font-family: "Open Sans", Arial, sans-serif;
    position: relative;
  }
  .card {
    position: absolute;
    width: 597px;
    height: 343px;
    overflow: hidden;
    box-shadow: 0 2px 8px rgba(0,0,0,0.12);
  }

  /* Back of card */
  .card-back {
    left: 80px; top: 70px;
    background: var(--brand-blue);
    border-radius: 10px;
  }
  .card-back .pattern-area {
    position: absolute; left: 0; top: 0;
    width: 200px; height: 100%;
    background: linear-gradient(90deg, var(--pale-blue) 0%, var(--brand-blue-soft) 55%, var(--brand-blue) 100%);
  }
  .card-back .brand {
    position: absolute; left: 225px; top: 142px;
  }

  /* Brand lockup */
  .brand { display: flex; align-items: center; gap: 12px; color: var(--white); font-weight: 700; }
  .brand-mark { width: 40px; height: 40px; background: var(--white); flex: none; }
  .brand-name { line-height: 1; white-space: nowrap; }
  .brand-name .line-main { display: block; font-size: 30px; letter-spacing: 1px; }
  .brand-name .line-sub { display: block; font-size: 11px; letter-spacing: 3.2px; margin-top: 3px; }

  /* Front of card */
  .card-front {
    left: 440px; top: 457px;
    background: var(--card-grey);
    border-bottom: 6px solid var(--card-edge);
  }
  .card-front .pattern-area {
    position: absolute; left: 0; top: 0;
    width: 240px; height: 100%;
    background: linear-gradient(90deg, var(--brand-blue-soft) 0%, var(--pale-blue) 60%, var(--card-grey) 100%);
  }
  .logo-band {
    position: absolute; left: 0; top: 48px;
    width: 262px; height: 92px;
    background: var(--brand-blue);
    padding: 18px 0 0 38px;
    box-shadow: 0 2px 4px rgba(0,0,0,0.15);
  }
  .logo-band .brand { gap: 8px; }
  .logo-band .brand-mark { width: 30px; height: 30px; }
  .logo-band .line-main { font-size: 21px; }
  .logo-band .line-sub { font-size: 8px; letter-spacing: 2.2px; }
  .tagline {
    position: absolute; left: 36px; bottom: 10px;
    color: var(--white); font-size: 8.2px; font-weight: 400; white-space: nowrap;
  }
  .contact-panel {
    position: absolute; left: 280px; top: 181px;
    width: 317px; height: 125px;
    background: var(--brand-blue);
    padding: 20px 0 0 20px;
    color: var(--white);
  }
  .contact-name { font-size: 16px; font-weight: 400; letter-spacing: 0.5px; text-transform: uppercase; }
  .contact-icons { list-style: none; margin: 6px 0 0 18px; }
  .contact-icons li { height: 15px; display: flex; align-items: center; }
  .contact-icons svg { width: 10px; height: 10px; fill: var(--white); }
</style>
</head>
<body>

<section class="card card-back" aria-label="Card back">
  <div class="pattern-area" role="img" aria-label="Scattered translucent blue and white squares"></div>
  <div class="brand">
    <span class="brand-mark"></span>
    <span class="brand-name">
      <span class="line-main">SUMMIT</span>
      <span class="line-sub">CIVIL WORKS GROUP</span>
    </span>
  </div>
</section>

<section class="card card-front" aria-label="Card front">
  <div class="pattern-area" role="img" aria-label="Scattered translucent blue squares"></div>
  <div class="logo-band">
    <div class="brand">
      <span class="brand-mark"></span>
      <span class="brand-name">
        <span class="line-main">SUMMIT</span>
        <span class="line-sub">CIVIL WORKS GROUP</span>
      </span>
    </div>
    <p class="tagline">Trusted Partners in Building and Site Delivery Services</p>
  </div>
  <div class="contact-panel">
    <p class="contact-name">Dorian</p>
    <ul class="contact-icons">
      <li aria-label="Mobile">
        <svg viewBox="0 0 10 10"><path d="M3 0h4a1 1 0 0 1 1 1v8a1 1 0 0 1-1 1H3a1 1 0 0 1-1-1V1a1 1 0 0 1 1-1zm0 1.5v6h4v-6z"/></svg>
      </li>
      <li aria-label="Email">
        <svg viewBox="0 0 10 10"><path d="M0 2h10v6H0z M0.5 2.3 5 5.5 9.5 2.3" stroke="#1b9bd7" stroke-width="0.8"/></svg>
      </li>
      <li aria-label="Postal address">
        <svg viewBox="0 0 10 10"><path d="M5 0.5 0 5h1.5v4.5h7V5H10z"/></svg>
      </li>
      <li aria-label="Website">
        <svg viewBox="0 0 10 10"><circle cx="5" cy="5" r="4.5"/><path d="M0.5 5h9M5 0.5v9M5 0.5c-2.4 2.6-2.4 6.4 0 9M5 0.5c2.4 2.6 2.4 6.4 0 9" stroke="#1b9bd7" stroke-width="0.6" fill="none"/></svg>
      </li>
    </ul>
  </div>
</section>

</body>
</html>
```